Business Card for Graphic Design Firm

This project is for a new graphic design firm based in New Jersey called Velmoric. We outsource graphic design and marketing jobs. We want to communicate that this is a professional company but it as well creative and artistic. This card may be used as a horizontal double sided paper card or a vertical single sided translucent card so feel free to submit designs in whichever format or both.
Updates

Reason: Extending the deadline because I'm not exactly satisfied with the designs so far.

Please view the updated project brief

Target Market(s)

Adults aged 25-60

Industry/Entity Type

Graphic Design

Font styles to use
Serif
Sans Serif

Requirements
Nice to have
• Maybe a triangular pattern around the edges similar to our logo

```html
<!DOCTYPE html>
<html lang="en">
<head>
<meta charset="utf-8">
<title>Velmoric Business Card</title>
<link rel="stylesheet" href="https://fonts.googleapis.com/css2?family=Montserrat:wght@300;400;600&display=swap">
<style>
  :root {
    --paper: #ffffff;
    --ink: #1b1b1b;
    --ink-soft: #6f6f6f;
    --brand-grey: #7b7d7e;
    --edge: #222222;
    --teal-deep: #127a92;
    --teal: #17a3b5;
    --sky: #7dcfe9;
    --orange: #f28322;
    --amber: #fbb121;
    --slate: #6d787d;
  }
  * { margin: 0; padding: 0; box-sizing: border-box; }
  html, body { width: 1200px; height: 848px; overflow: hidden; background: var(--paper); }
  .canvas { position: relative; width: 1200px; height: 848px; font-family: "Montserrat", sans-serif; }
  .card-shapes { position: absolute; inset: 0; }
  .card-front__text { position: absolute; left: 157px; color: var(--ink-soft); font-weight: 300; }
  .holder { top: 370px; font-size: 14px; color: var(--ink-soft); white-space: nowrap; }
  .holder__name { font-weight: 600; color: var(--ink); }
  .contact { top: 428px; font-size: 13.5px; line-height: 19.3px; list-style: none; white-space: nowrap; }
  .brand-name {
    position: absolute; right: 658px; top: 509px;
    font-size: 34px; font-weight: 400; letter-spacing: 1.5px; color: var(--brand-grey);
    white-space: nowrap;
  }
</style>
</head>
<body>
<main class="canvas">
  <svg class="card-shapes" width="1200" height="848" viewBox="0 0 1200 848">
    <defs>
      <linearGradient id="pattern-tones" x1="0" y1="0" x2="1" y2="1">
        <stop offset="0" stop-color="var(--teal)"/>
        <stop offset="0.3" stop-color="var(--amber)"/>
        <stop offset="0.55" stop-color="var(--teal-deep)"/>
        <stop offset="0.8" stop-color="var(--orange)"/>
        <stop offset="1" stop-color="var(--sky)"/>
      </linearGradient>
    </defs>
    <polygon class="card-front" points="114,288 562,288 562,562 114,562 114,428 136,374 114,322"
             fill="var(--paper)" stroke="var(--edge)" stroke-width="1.2"/>
    <polygon class="card-back" role="img" aria-label="Triangle mosaic pattern in teal, sky blue, orange, amber and slate"
             points="630,288 1078,288 1078,340 1055,382 1078,426 1078,562 630,562"
             fill="url(#pattern-tones)" stroke="var(--edge)" stroke-width="1.2"/>
  </svg>

  <p class="card-front__text holder"><span class="holder__name">Daniel Okafor</span> Marketing Executive</p>
  <ul class="card-front__text contact">
    <li>48 Linden Avenue, Brookfield, CT</li>
    <li>+1 555-019-2740</li>
    <li>daniel@velmoric.com</li>
    <li>www.velmoric.com</li>
  </ul>
  <p class="brand-name">VELMORIC</p>
</main>
</body>
</html>
```